Calloway needs a modernized design

We would like a modern update (that can be responsive) to our existing website. Attached are the two existing pages we would like new concepts of - our home page and a page about one of our locations.

Calloway is provides executive offices and virtual office services. Startups, law firms, and financial services are our primary clients. We would like a professional, clean design, leaning towards minimalist. We intend to greatly reduce/eliminate the long paragraphs of text.

Industry/Entity Type

Business Service

Number of Pages Required

2 page

Requirements
Must have
• A design that can be responsive
Nice to have
• Large image(s) on home page that rotate.

```html
<!DOCTYPE html>
<html lang="en">
<head>
<meta charset="utf-8">
<title>Calloway Business Centers</title>
<link href="https://fonts.googleapis.com/css2?family=Open+Sans:wght@300;400;600&display=swap" rel="stylesheet">
<style>
:root{
  --navy:#233568;
  --navy-dark:#1f2f5e;
  --ink:#2b2b2b;
  --text:#555;
  --muted:#777;
  --line:#e2e2e2;
  --band:#f4f5f7;
  --white:#fff;
  --hex:#333;
}
*{box-sizing:border-box;margin:0;padding:0}
html,body{width:770px;height:1200px;overflow:hidden;background:var(--white)}
body{font-family:"Open Sans",Arial,sans-serif;color:var(--ink);position:relative}
.abs{position:absolute}
.topbar{left:0;top:0;width:770px;height:24px;background:var(--navy);color:var(--white);font-size:7.5px;display:flex;align-items:center;padding:0 58px;justify-content:space-between}
.topbar .phones{display:flex;align-items:center;gap:5px}
.social{display:flex;gap:5px}
.social span{width:14px;height:14px;border-radius:50%;background:#3b5998;display:block}
.social span:nth-child(2){background:#2aa8e0}
.social span:nth-child(3){background:#d8352a}
.social span:nth-child(4){background:var(--navy-dark);border:1px solid #3c4f85}
.header{left:0;top:24px;width:770px;height:46px;border-bottom:1px solid var(--line);background:var(--white)}
.brand{left:58px;top:8px;display:flex;align-items:center;gap:5px}
.brand-dot{width:30px;height:30px;border-radius:50%;background:var(--navy)}
.brand-name{font-size:13px;color:var(--navy);line-height:1}
.brand-name small{display:block;font-size:5.5px;letter-spacing:.5px;margin-top:2px}
.nav{right:57px;top:12px;display:flex;align-items:center;gap:13px;font-size:7px;text-transform:uppercase;color:#333}
.nav .active{background:var(--navy);color:var(--white);border-radius:11px;padding:0 18px;height:22px;line-height:22px}
.hero{left:0;top:70px;width:770px;height:302px;background:linear-gradient(90deg,#f3f4f6 0%,#e9ecef 30%,#6d7486 48%,#4e5668 65%,#c9ced6 85%,#eef0f3 100%)}
.hero-title{left:70px;top:92px;font-size:31px;font-weight:400;color:var(--navy);letter-spacing:.5px}
.hero-sub{left:73px;top:128px;font-size:13px;color:var(--navy);line-height:18px}
.arrow{top:131px;width:30px;height:30px;border-radius:50%;display:flex;align-items:center;justify-content:center}
.arrow.prev{left:14px;background:var(--navy)}
.arrow.next{right:14px;background:var(--white)}
.tabs{left:56px;top:402px;width:158px}
.tab{height:30px;line-height:30px;font-size:7.5px;padding-left:15px;border-bottom:1px solid var(--line);color:#333;text-transform:uppercase}
.tab.active{background:var(--navy);color:var(--white);border:none;position:relative}
.tab.active:after{content:"";position:absolute;right:-6px;top:9px;border-left:6px solid var(--navy);border-top:6px solid transparent;border-bottom:6px solid transparent}
.tab-scroll{left:211px;top:441px;width:2px;height:41px;background:#ddd}
.suite-photo{left:226px;top:401px;width:304px;height:203px;background:linear-gradient(120deg,#8a97a8,#d9dde2 45%,#2b3145 70%,#c9cbcf)}
.suite-card{left:446px;top:417px;width:266px;height:173px;background:var(--white);border:1px solid var(--line);padding:30px 34px}
.suite-card h2{font-size:14px;font-weight:400;letter-spacing:.6px;color:var(--ink);margin-bottom:10px}
.suite-card p{font-size:6.6px;line-height:12.5px;color:var(--muted)}
.btn{display:inline-block;background:var(--navy);color:var(--white);font-size:7px;text-transform:uppercase;border-radius:11px;height:22px;line-height:22px;padding:0 12px}
.suite-card .btn{margin-top:10px}
.industries{left:0;top:658px;width:770px;height:109px;background:var(--band)}
.industry{top:630px;width:200px;text-align:center}
.industry svg{display:block;margin:0 auto}
.industry h3{font-size:10px;font-weight:400;margin-top:11px;letter-spacing:.3px}
.industry p{font-size:6.8px;line-height:12.5px;color:var(--text);margin-top:4px}
.value-title{right:286px;top:798px;font-size:15px;font-weight:400;letter-spacing:.5px}
.value-text{left:60px;top:823px;width:426px;font-size:6.9px;line-height:14.3px;color:var(--text);text-align:justify;text-align-last:right}
.value .btn{left:423px;top:916px;position:absolute}
.value-art{left:505px;top:778px}
.contact{left:0;top:986px;width:770px;height:184px;background:var(--band)}
.contact-title{left:57px;top:1000px;font-size:14px;font-weight:400;color:var(--navy);letter-spacing:.4px}
.field{background:var(--white);border:1px solid #dcdcdc;font-size:7px;color:#666;padding:4px 8px}
.contact-info{left:382px;top:1028px;font-size:7px;color:#333;line-height:12px}
.info-row{display:flex;gap:8px;margin-bottom:7px}
.info-row svg{flex:none;margin-top:1px}
.map{left:540px;top:1028px;width:172px;height:104px;background:linear-gradient(135deg,#e8e6de,#dfe8d6 50%,#ece9e1)}
.footer{left:0;top:1170px;width:770px;height:30px;background:var(--navy);color:var(--white);font-size:7.3px;display:flex;align-items:center;justify-content:space-between;padding:0 58px}
.footer nav{display:flex;gap:10px}
</style>
</head>
<body>

<div class="abs topbar">
  <div class="phones">
    <svg width="8" height="8" viewBox="0 0 24 24"><path fill="#fff" d="M6.6 10.8a15 15 0 006.6 6.6l2.2-2.2a1 1 0 011-.25 11.4 11.4 0 003.6.6 1 1 0 011 1V20a1 1 0 01-1 1A17 17 0 013 4a1 1 0 011-1h3.5a1 1 0 011 1c0 1.25.2 2.45.6 3.6a1 1 0 01-.25 1z"/></svg>
    Dallas 214.555.0142 | Houston 713.555.0187
  </div>
  <div class="social"><span></span><span></span><span></span><span></span></div>
</div>

<header class="abs header">
  <div class="abs brand"><span class="brand-dot"></span><span class="brand-name">CALLOWAY<small>BUSINESS CENTERS</small></span></div>
  <nav class="abs nav">
    <span class="active">Home</span><span>Properties</span><span>Virtual Tours &amp; Videos</span><span>Photos</span><span>Broker Referrals</span>
  </nav>
</header>

<section class="abs hero" role="img" aria-label="Three smiling businessmen in suits working together at a computer in a bright office"></section>
<h1 class="abs hero-title">ON DEMAND</h1>
<p class="abs hero-sub">Meeting Rooooms That Fit<br>Your Needs</p>
<div class="abs arrow prev"><svg width="8" height="8" viewBox="0 0 10 10"><path d="M7 1L3 5l4 4" fill="none" stroke="#fff" stroke-width="1.5"/></svg></div>
<div class="abs arrow next"><svg width="8" height="8" viewBox="0 0 10 10"><path d="M3 1l4 4-4 4" fill="none" stroke="#233568" stroke-width="1.5"/></svg></div>

<div class="abs tabs">
  <div class="tab active">Executive Office Suites</div>
  <div class="tab">On-Deman Meeting Rooms</div>
  <div class="tab">On-Demand Training Rooms</div>
  <div class="tab">Virtual Office Solutions</div>
  <div class="tab" style="border:none">Video Conference Solutions</div>
</div>
<div class="abs tab-scroll"></div>
<div class="abs suite-photo" role="img" aria-label="Businessman working on a laptop at a desk beside a window"></div>
<div class="abs suite-card">
  <h2>EXECUTIVE OFFICE SUITES</h2>
  <p>Lorem ipsum dolor sit amet, consectetuer adipiscing elit. Aenean commodo ligula eget dolor. Aenean massa. Cum sociis natoque penatibus et magnis dis parturient montes, nascetur ridiculus mus.</p>
  <span class="btn">Read More</span>
</div>

<div class="abs industries"></div>
<div class="abs industry" style="left:73px">
  <svg width="50" height="55" viewBox="0 0 50 55"><polygon points="25,0 50,14 50,41 25,55 0,41 0,14" fill="#333"/><rect x="15" y="19" width="18" height="14" fill="none" stroke="#fff" stroke-width="1.5"/><rect x="19" y="26" width="2" height="5" fill="#fff"/><rect x="23" y="23" width="2" height="8" fill="#fff"/><circle cx="33" cy="30" r="3" fill="#fff"/></svg>
  <h3>STARTUPS</h3>
  <p>Lorem ipsum dolor sit amet, consectetuer adipiscing elit. Aenean commodo ligula eget dolor. Aenean massa. Cum sociis natoque.</p>
</div>
<div class="abs industry" style="left:280px">
  <svg width="50" height="55" viewBox="0 0 50 55"><polygon points="25,0 50,14 50,41 25,55 0,41 0,14" fill="#233568"/><path d="M25 17v20M18 37h14M15 21h20" stroke="#fff" stroke-width="1.5" fill="none"/><path d="M12 30l3-9 3 9zM32 30l3-9 3 9z" fill="none" stroke="#fff" stroke-width="1.2"/></svg>
  <h3>LAW FIRMS</h3>
  <p>Lorem ipsum dolor sit amet, consectetuer adipiscing elit. Aenean commodo ligula eget dolor. Aenean massa. Cum sociis natoque.</p>
</div>
<div class="abs industry" style="left:486px">
  <svg width="50" height="55" viewBox="0 0 50 55"><polygon points="25,0 50,14 50,41 25,55 0,41 0,14" fill="#333"/><rect x="17" y="18" width="18" height="13" fill="none" stroke="#fff" stroke-width="1.5"/><rect x="13" y="23" width="18" height="13" fill="#333" stroke="#fff" stroke-width="1.5"/><circle cx="22" cy="29.5" r="2.5" fill="#fff"/></svg>
  <h3>FINANCIAL</h3>
  <p>Lorem ipsum dolor sit amet, consectetuer adipiscing elit. Aenean commodo ligula eget dolor. Aenean massa. Cum sociis natoque.</p>
</div>

<section class="value">
  <h2 class="abs value-title">VALUE</h2>
  <p class="abs value-text">Either you need Dallas/Ft. Worth Office Space, Dallas Executive Suites, Ft. Worth Executive Suites, Houston Office Space, Houston Executive Suites, or maybe you simply need a place to stop in and use an on-demand office or meeting room from time to time or utilize ourt local business phone numbers, phone answering or business addresses through one of our virtual office solutions. At Calloway, you will always find affordable and beautiful, professional properties. To make decisions easy for our full service executive suite clients, we include everything in one upfront and honest price - including the office, phone answering and 55 hours of conference room time per month (alone a value of over $1,600/mo).</p>
  <span class="btn">Read More</span>
  <svg class="abs value-art" width="200" height="198" viewBox="0 0 200 198" role="img" aria-label="Two colleagues reviewing work together at a laptop, framed in a diamond">
    <defs><linearGradient id="vg" x1="0" y1="0" x2="1" y2="1"><stop offset="0" stop-color="#b9c3cf"/><stop offset=".5" stop-color="#8d7a6c"/><stop offset="1" stop-color="#e6e8ec"/></linearGradient></defs>
    <polygon points="70,8 196,42 160,196 30,160" fill="none" stroke="#d8d8d8" stroke-width="1"/>
    <polygon points="98,2 194,99 98,196 2,99" fill="url(#vg)" stroke="#222" stroke-width="1.5"/>
  </svg>
</section>

<section class="abs contact"></section>
<h2 class="abs contact-title">CONTACT US</h2>
<div class="abs field" style="left:57px;top:1030px;width:152px;height:19px">Name</div>
<div class="abs field" style="left:216px;top:1030px;width:151px;height:19px">Email</div>
<div class="abs field" style="left:57px;top:1055px;width:310px;height:67px">Message</div>
<span class="abs btn" style="left:57px;top:1131px;width:67px;height:23px;text-align:center">Submit</span>
<div class="abs contact-info">
  <div class="info-row"><svg width="10" height="8" viewBox="0 0 12 9"><rect x=".5" y=".5" width="11" height="8" fill="none" stroke="#233568"/><path d="M.5.5L6 5l5.5-4.5" fill="none" stroke="#233568"/></svg><span>Offices@CallowayOffices.com</span></div>
  <div class="info-row" style="margin-top:10px"><svg width="10" height="10" viewBox="0 0 24 24"><path fill="#233568" d="M6.6 10.8a15 15 0 006.6 6.6l2.2-2.2a1 1 0 011-.25 11.4 11.4 0 003.6.6 1 1 0 011 1V20a1 1 0 01-1 1A17 17 0 013 4a1 1 0 011-1h3.5a1 1 0 011 1c0 1.25.2 2.45.6 3.6a1 1 0 01-.25 1z"/></svg><span>Houston 713.555.0187<br>Dallas 214.555.0142</span></div>
  <div class="info-row" style="margin-top:10px"><svg width="12" height="12" viewBox="0 0 12 12"><path d="M4 1a3 3 0 013 3c0 2-3 5-3 5S1 6 1 4a3 3 0 013-3z" fill="none" stroke="#233568"/><circle cx="4" cy="4" r="1" fill="#233568"/><path d="M1 11h10M8 8l3 3" stroke="#233568" fill="none"/></svg><span>Calloway Business Centers 4120 N.<br>Harwell Parkway Suite 300 Dallas,<br>Texas 75204</span></div>
</div>
<div class="abs map" role="img" aria-label="Street map showing the office location with a pin marker"></div>

<footer class="abs footer">
  <span>Copyright 2016 . All Rights Reserved</span>
  <nav><span>About Us</span><span>Contact Us</span><span>Testimonials</span><span>FAQs</span><span>Careers</span><span>Furniture</span><span>Specials</span><span>Site Map</span><span>Privacy</span></nav>
</footer>

</body>
</html>
```